Automotive Brand Survey Online

Hi guys, we are looking for a freelancer who can design User Interface design (UI) for a survey-online website layout. <br/><br/>For the content, there are question, choices, back and next buttons - as if you are designing a survey website.<br/><br/>There are 5 main contents of the website consists of:<br/>1. Single-answer question<br/>2. Yes/No-answer question<br/>3. Net Promoter Score (NPS) or 1-5 scale question<br/>4. Open-end question<br/>5. Thank you page when finish survey<br/><br/>Here is the demo and more description<br/>https://preview.quorvane.site/survey/
Target Market(s)
Car Owner
Industry/Entity Type
Automotive
Number of Pages Required
1 page

```html
<!DOCTYPE html>
<html lang="en">
<head>
<meta charset="utf-8">
<title>Varnok Survey – Thank You</title>
<link href="https://fonts.googleapis.com/css2?family=Poppins:wght@400;500;600&family=Lato:wght@400;700&display=swap" rel="stylesheet">
<style>
  :root {
    --page-bg: #f3f3f3;
    --ink: #262626;
    --muted: #6a6a6a;
    --brand-purple: #633b64;
    --logo-dark: #2b2b2b;
    --logo-light: #f1f1f1;
    --white: #ffffff;
  }
  * { margin: 0; padding: 0; box-sizing: border-box; }
  html, body {
    width: 1200px;
    height: 2700px;
    overflow: hidden;
    background: var(--page-bg);
  }
  .survey-page {
    position: relative;
    width: 1200px;
    height: 2700px;
    color: var(--ink);
    font-family: "Lato", sans-serif;
  }
  .brand-tile {
    position: absolute;
    left: 412px;
    top: 112px;
    width: 376px;
    height: 376px;
    border-radius: 38px;
    background: var(--logo-dark);
    display: flex;
    align-items: center;
    justify-content: center;
  }
  .brand-name {
    font-family: "Poppins", sans-serif;
    font-weight: 500;
    font-size: 74px;
    letter-spacing: 3px;
    color: var(--logo-light);
  }
  .progress-label {
    position: absolute;
    left: 94px;
    right: 94px;
    top: 535px;
    display: flex;
    justify-content: space-between;
    font-family: "Lato", sans-serif;
    font-weight: 700;
    font-size: 54px;
    line-height: 1;
  }
  .progress-track {
    position: absolute;
    left: 75px;
    top: 652px;
    width: 1050px;
    height: 38px;
    border-radius: 19px;
    background: var(--brand-purple);
  }
  .done-icon {
    position: absolute;
    left: 521px;
    top: 795px;
    width: 158px;
    height: 158px;
  }
  .thanks-title {
    position: absolute;
    left: 0;
    right: 0;
    top: 1005px;
    text-align: center;
    font-family: "Poppins", sans-serif;
    font-weight: 600;
    font-size: 142px;
    line-height: 161px;
    letter-spacing: 1px;
  }
  .thanks-subtitle {
    position: absolute;
    left: 0;
    right: 0;
    top: 1535px;
    text-align: center;
    font-family: "Lato", sans-serif;
    font-size: 49px;
    color: var(--muted);
  }
  .thanks-body {
    position: absolute;
    left: 90px;
    right: 90px;
    top: 1645px;
    text-align: center;
    font-family: "Lato", sans-serif;
    font-size: 58px;
    line-height: 82px;
    hyphens: auto;
  }
  .return-button {
    position: absolute;
    left: 75px;
    top: 2317px;
    width: 1050px;
    height: 184px;
    border-radius: 20px;
    background: var(--brand-purple);
    color: var(--white);
    display: flex;
    align-items: center;
    justify-content: center;
    font-family: "Poppins", sans-serif;
    font-size: 64px;
    text-decoration: none;
  }
</style>
</head>
<body>
  <main class="survey-page">
    <div class="brand-tile"><span class="brand-name">VARNOK</span></div>

    <div class="progress-label">
      <span>Survey Progress</span>
      <span>100%</span>
    </div>
    <div class="progress-track"></div>

    <svg class="done-icon" viewBox="0 0 158 158" aria-hidden="true">
      <circle cx="79" cy="79" r="79" fill="var(--brand-purple)"/>
      <path d="M52 81 L71 99 L107 62" fill="none" stroke="#ffffff" stroke-width="15" stroke-linecap="round" stroke-linejoin="round"/>
    </svg>

    <h1 class="thanks-title">Thank you<br>for completing<br>the survey</h1>
    <p class="thanks-subtitle">We hope you enjoye the survey</p>
    <p class="thanks-body">Lorem ipsum dolor sit amet, consecte-tur adipiscing elit. In sed est velit. Cras pellentesque ipsum a lectus dignissim feugiat. Curabitur sit amet nisi nibh. Sed iaculis volutpat ultricies. Mauris eget risus posuere, malesuada nisi ut, venenatis lorem.</p>

    <a class="return-button" href="https://preview.quorvane.site/survey/">Return to Survey</a>
  </main>
</body>
</html>
```